Scrap Metal Recycling

We are looking for a simple yet bold business card. We already have the logo, please see attached. Color scheme of blue, black and white or just blue and white.

```html
<!DOCTYPE html>
<html lang="en">
<head>
<meta charset="utf-8">
<title>Norvale Metals Inc. – Business Card</title>
<link href="https://fonts.googleapis.com/css2?family=Montserrat:wght@400;500;700&display=swap" rel="stylesheet">
<style>
  :root {
    --stage: #e6e7e9;
    --card-white: #ffffff;
    --charcoal: #3a3a3a;
    --ink: #3b3b3b;
    --deep: #0b0b0b;
    --accent: #1a8fad;
    --paper-text: #ffffff;
  }
  * { margin: 0; padding: 0; box-sizing: border-box; }
  html, body {
    width: 1048px; height: 1200px; overflow: hidden;
    background: var(--stage);
    font-family: "Montserrat", sans-serif;
  }
  .card {
    position: absolute;
    width: 843px; height: 482px;
    overflow: hidden;
    box-shadow: 0 6px 22px rgba(0,0,0,0.18);
  }
  .card--front { left: 84px; top: 87px; background: var(--card-white); }
  .card--back  { left: 77px; top: 623px; background: var(--charcoal); }

  .brand-mark { position: absolute; }
  .brand-name {
    font-weight: 700; font-size: 36px; letter-spacing: -0.5px;
    line-height: 1; white-space: nowrap;
  }
  .brand-tagline {
    margin-top: 14px;
    font-weight: 500; font-size: 21px; letter-spacing: 7.2px;
    color: var(--accent); white-space: nowrap;
  }
  .card--front .brand-mark { left: 44px; top: 92px; }
  .card--front .brand-name { color: var(--ink); }
  .card--back .brand-mark { right: 36px; top: 92px; text-align: right; }
  .card--back .brand-name { color: var(--paper-text); }

  .decor { position: absolute; }
  .decor--front { left: 440px; top: 0; width: 403px; height: 482px; }
  .decor--back  { left: 0; top: 0; width: 560px; height: 482px; }

  .contact { position: absolute; left: 44px; top: 218px; color: var(--ink); }
  .contact__name {
    font-weight: 700; font-size: 35px; letter-spacing: -1px;
    color: var(--accent); line-height: 1;
  }
  .contact__role { margin-top: 12px; font-size: 21px; font-weight: 400; }
  .contact__list { list-style: none; margin-top: 10px; }
  .contact__item {
    display: flex; align-items: center; gap: 14px;
    font-size: 21px; height: 31px;
  }
  .contact__icon { width: 19px; height: 19px; flex: none; }
  .contact__address { margin-top: 14px; font-size: 21px; line-height: 32px; }
</style>
</head>
<body>

<section class="card card--front">
  <svg class="decor decor--front" viewBox="0 0 403 482" role="img" aria-label="Large brand symbol decoration">
    <circle cx="260" cy="260" r="250" fill="var(--charcoal)"/>
  </svg>

  <div class="brand-mark">
    <div class="brand-name">NORVALE METALS INC.</div>
    <div class="brand-tagline">SCRAP METAL RECYCLING</div>
  </div>

  <div class="contact">
    <div class="contact__name">JONATHAN SMITH</div>
    <div class="contact__role">Managing Director</div>
    <ul class="contact__list">
      <li class="contact__item">
        <svg class="contact__icon" viewBox="0 0 24 24"><path fill="var(--accent)" d="M6.6 10.8a15 15 0 0 0 6.6 6.6l2.2-2.2a1 1 0 0 1 1-.25 11.4 11.4 0 0 0 3.6.57 1 1 0 0 1 1 1V20a1 1 0 0 1-1 1A17 17 0 0 1 3 4a1 1 0 0 1 1-1h3.5a1 1 0 0 1 1 1c0 1.25.2 2.45.57 3.57a1 1 0 0 1-.25 1z"/></svg>
        044-123 456 789
      </li>
      <li class="contact__item">
        <svg class="contact__icon" viewBox="0 0 24 24"><rect x="2" y="5" width="20" height="14" fill="var(--accent)"/><path d="M2 5l10 8 10-8" fill="none" stroke="#fff" stroke-width="1.5"/></svg>
        info@webname.com
      </li>
      <li class="contact__item">
        <svg class="contact__icon" viewBox="0 0 24 24"><circle cx="12" cy="12" r="10" fill="var(--accent)"/><path d="M2 12h20M12 2c3 3 3 17 0 20M12 2c-3 3-3 17 0 20" fill="none" stroke="#fff" stroke-width="1.3"/></svg>
        www.websitename.com
      </li>
    </ul>
    <div class="contact__address">421, Address line here<br>Country Name, 45452</div>
  </div>
</section>

<section class="card card--back">
  <svg class="decor decor--back" viewBox="0 0 560 482" role="img" aria-label="Large shaded brand symbol decoration">
    <defs>
      <linearGradient id="decorShade" x1="0" y1="0" x2="1" y2="0.6">
        <stop offset="0" stop-color="var(--deep)"/>
        <stop offset="0.55" stop-color="#1c1c1c"/>
        <stop offset="1" stop-color="#7a7a7a"/>
      </linearGradient>
    </defs>
    <circle cx="200" cy="300" r="280" fill="url(#decorShade)"/>
  </svg>

  <div class="brand-mark">
    <div class="brand-name">NORVALE METALS INC.</div>
    <div class="brand-tagline">SCRAP METAL RECYCLING</div>
  </div>
</section>

</body>
</html>
```